We're Hiring Poster or Flyer design

We’re Hiring Details:

Positions include:
Office Manager
Office Assistant
Data Entry Techs
Outreach Manager
Asst. Outreach Manager
Events Coordinator
Drivers (must have personal car, insurance & Driver’s License)
Outreach Specialist—Walkers
Outreach Specialist—Phone/Telemarketing (evenings only)

Excellent Pay ! Fun Atmosphere ! Bonus Pay with Promotional & Career Advancement Opportunities

***************
need 3 formats of SAME flyer:
1) 8.5 x 11
2) 8.5 x 14
3) 11 x17

creative and eye catching a must; this flyer will be used on college bulletin boards and used to attract a younger demographic . . hip and chic look with "Americana style or political motif" preferred.

Target Market(s)

younger demographic . . flyer will be used during college recruiting fairs and in younger settings---age BRACKET is 21 - 35 Years old

Industry/Entity Type

Employment Agency

Font styles to use
Sans Serif

Colors

Designer to choose colors to be used in the design.

Requirements
Must have
• clean and attractive; hip; chic; simple and with good stock pics and layout
Nice to have
• american flag and patriotism
Should not have
• too much details on the job -- I only included the job announcement so you can get an idea of WHAT and WHO I am looking for . . don't list all the BORING details on the flyer/poster

```html
<!DOCTYPE html>
<html lang="en">
<head>
<meta charset="utf-8">
<title>We're Hiring – Flyer Formats</title>
<link href="https://fonts.googleapis.com/css2?family=Exo+2:wght@400;700;800&family=Oswald:wght@400;500;600&display=swap" rel="stylesheet">
<style>
  :root{
    --navy:#1d3a70;
    --navy-deep:#17305f;
    --orange:#f47a20;
    --white:#ffffff;
    --ink:#1b2b4d;
    --stage:#ece7e0;
    --photo-a:#e8ebef;
    --photo-b:#c3c9d2;
    --photo-c:#dde1e7;
    --photo-d:#a9b0ba;
  }
  *{box-sizing:border-box;margin:0;padding:0}
  html,body{width:1200px;height:713px;overflow:hidden}
  body{background:var(--stage);position:relative;font-family:"Oswald",sans-serif}

  .flyer{position:absolute;overflow:hidden;box-shadow:0 2px 6px rgba(0,0,0,.25)}

  .flyer--11x17{left:47px;top:40px;width:412px;height:636px;
    --h:1;--head-l:21px;--head-t:14px;
    --cand-r:19px;--cand-t:72px;
    --t:1;--list-l:41px;--list-top:161px;--row:20.4px;
    --p:1;--panel-l:16px;--panel-w:217px;--panel-h:206px;--panel-b:0px;
    --board-l:238px;--board-t:485px;--board-w:155px;
    --badge-l:286px;--badge-t:548px;--badge-w:52px;--badge-h:40px;
    --flag-h:210px;}
  .flyer--8x14{left:501px;top:152px;width:319px;height:524px;
    --h:.82;--head-l:10px;--head-t:12px;
    --cand-r:9px;--cand-t:64px;
    --t:.81;--list-l:28px;--list-top:135px;--row:16.4px;
    --p:.81;--panel-l:7px;--panel-w:175px;--panel-h:159px;--panel-b:0px;
    --board-l:200px;--board-t:396px;--board-w:118px;
    --badge-l:226px;--badge-t:448px;--badge-w:54px;--badge-h:34px;
    --flag-h:190px;}
  .flyer--8x11{left:842px;top:265px;width:319px;height:411px;
    --h:.6;--head-l:33px;--head-t:8px;
    --cand-r:31px;--cand-t:36px;
    --t:.69;--list-l:46px;--list-top:102px;--row:13.3px;
    --p:.7;--panel-l:30px;--panel-w:149px;--panel-h:118px;--panel-b:6px;
    --board-l:196px;--board-t:312px;--board-w:84px;
    --badge-l:216px;--badge-t:355px;--badge-w:46px;--badge-h:28px;
    --flag-h:160px;}

  .photo{position:absolute;inset:0;
    background:linear-gradient(90deg,var(--photo-a) 0%,var(--photo-b) 28%,var(--photo-c) 48%,var(--photo-b) 62%,var(--photo-d) 85%,var(--photo-c) 100%)}
  .flag{position:absolute;left:0;right:0;bottom:0;height:var(--flag-h);
    background:linear-gradient(165deg,rgba(255,255,255,0) 0%,rgba(255,255,255,0) 18%,#e8d4d6 22%,#c8333e 40%,#efe6e6 58%,#bf2531 78%,#e9dede 100%);
    clip-path:polygon(0 30%,100% 0,100% 100%,0 100%)}
  .flag::after{content:"";position:absolute;left:0;bottom:0;width:45%;height:55%;
    background:linear-gradient(160deg,#3a4f86,#1f3468)}

  .headline{position:absolute;left:var(--head-l);top:var(--head-t);
    font-family:"Exo 2",sans-serif;color:var(--navy);line-height:.9}
  .headline .were{display:block;font-weight:400;font-size:calc(60px * var(--h));letter-spacing:-1px}
  .headline .hiring{display:block;font-weight:800;font-size:calc(72px * var(--h));letter-spacing:-1px}

  .candidate{position:absolute;right:var(--cand-r);top:var(--cand-t);
    display:flex;align-items:center;gap:calc(6px * var(--h))}
  .candidate .mark{width:calc(9px * var(--h));height:calc(9px * var(--h));background:var(--orange);flex:none}
  .candidate .name{font-family:"Exo 2",sans-serif;font-weight:800;color:var(--navy);
    font-size:calc(22px * var(--h));line-height:1.05;text-align:center}

  .positions{position:absolute;left:var(--list-l);top:var(--list-top);color:var(--ink)}
  .positions h2{font-weight:600;font-size:calc(20px * var(--t));line-height:calc(24px * var(--t));
    letter-spacing:.2px;margin-bottom:calc(10px * var(--t))}
  .positions ul{list-style:none}
  .positions li{position:relative;padding-left:calc(10px * var(--t));
    font-weight:500;font-size:calc(18px * var(--t));line-height:var(--row);white-space:nowrap}
  .positions li::before{content:"";position:absolute;left:0;top:calc(var(--row) / 2);
    width:calc(5px * var(--t));height:calc(5px * var(--t));border-radius:50%;
    background:var(--orange);transform:translateY(-50%)}
  .positions .note{display:block;font-weight:400;font-size:calc(13.5px * var(--t));
    line-height:var(--row);margin-left:calc(-2px * var(--t))}

  .perks{position:absolute;left:var(--panel-l);bottom:var(--panel-b);width:var(--panel-w);height:var(--panel-h);
    color:var(--white);padding:calc(24px * var(--p)) calc(8px * var(--p)) 0 calc(14px * var(--p))}
  .perks > svg{position:absolute;inset:0;width:100%;height:100%;z-index:0}
  .perks > *:not(svg){position:relative;z-index:1}
  .perks ul{list-style:none}
  .perks li{position:relative;padding-left:calc(17px * var(--p));
    font-weight:500;text-transform:uppercase;font-size:calc(13.5px * var(--p));line-height:calc(20.5px * var(--p))}
  .perks li::before{content:"★";position:absolute;left:0;top:0}
  .perks .contact{margin-top:calc(10px * var(--p));font-weight:600;font-size:calc(12.5px * var(--p));line-height:1.3}
  .perks .phone{display:flex;align-items:center;gap:calc(5px * var(--p));
    font-size:calc(15px * var(--p));font-weight:600;line-height:1.3}
  .perks .phone svg{width:calc(12px * var(--p));height:calc(12px * var(--p))}

  .board{position:absolute;left:var(--board-l);top:var(--board-t);width:var(--board-w);font-style:normal;
    color:var(--navy-deep);font-weight:500;text-transform:uppercase;
    font-size:calc(8.5px * var(--t));line-height:1.3;text-align:center}
  .board .street{margin-top:calc(5px * var(--t));text-transform:none;font-size:calc(9.5px * var(--t))}
  .badge{position:absolute;left:var(--badge-l);top:var(--badge-t);width:var(--badge-w);height:var(--badge-h);
    background:var(--white);border:1px solid #cfd3da}
</style>
</head>
<body>

<article class="flyer flyer--11x17">
  <div class="photo" role="img" aria-label="Smiling young professional in a grey pinstripe suit and tie"></div>
  <div class="flag" role="img" aria-label="Waving American flag"></div>
  <h1 class="headline"><span class="were">WE’RE</span><span class="hiring">HIRING</span></h1>
  <p class="candidate"><span class="mark"></span><span class="name">Marco<br>Delgado<br>Mayor</span></p>
  <section class="positions">
    <h2>JOB POSITIONS INCLUDE:</h2>
    <ul>
      <li>Office Manager</li>
      <li>Office Assistant</li>
      <li>Data Entry Techs</li>
      <li>Outreach Manager</li>
      <li>Asst. Outreach Manager</li>
      <li>Events Coordinator</li>
      <li>Drivers<span class="note">(must have personal car,&nbsp; insurance &amp; Driver’s License)</span></li>
      <li>Outreach Specialist - Walkers</li>
      <li>Outreach Specialist - Phone/ Telemarketing<span class="note">(evenings only)</span></li>
    </ul>
  </section>
  <aside class="perks">
    <svg viewBox="0 0 217 206" preserveAspectRatio="none" aria-hidden="true"><polygon points="0,14 175,14 197,0 217,12 217,206 0,206" fill="#1d3a70"/></svg>
    <ul>
      <li>Excellent Pay !</li>
      <li>Fun Atmosphere</li>
      <li>Bonus Pay with Promotional<br>&amp; Career Advancement<br>Opportunities</li>
    </ul>
    <p class="contact">Questions call Renata Cole at</p>
    <p class="phone"><svg viewBox="0 0 24 24" aria-hidden="true"><circle cx="12" cy="12" r="11" fill="none" stroke="#fff" stroke-width="2"/><path d="M8 6l2 0 1 3-1.5 1.2a8 8 0 0 0 4.3 4.3L15 13l3 1v2c0 1-1 2-2 2A10 10 0 0 1 6 8c0-1 1-2 2-2z" fill="#fff"/></svg>909.555.0142</p>
  </aside>
  <address class="board">Ridgeview County<br>Workforce Board<div class="street">412 West Oak Lane (Suite 200)<br>Ridgeview, CA 92410</div></address>
  <div class="badge"></div>
</article>

<article class="flyer flyer--8x14">
  <div class="photo" role="img" aria-label="Smiling young professional in a grey pinstripe suit and tie"></div>
  <div class="flag" role="img" aria-label="Waving American flag"></div>
  <h1 class="headline"><span class="were">WE’RE</span><span class="hiring">HIRING</span></h1>
  <p class="candidate"><span class="mark"></span><span class="name">Marco<br>Delgado<br>Mayor</span></p>
  <section class="positions">
    <h2>JOB POSITIONS INCLUDE:</h2>
    <ul>
      <li>Office Manager</li>
      <li>Office Assistant</li>
      <li>Data Entry Techs</li>
      <li>Outreach Manager</li>
      <li>Asst. Outreach Manager</li>
      <li>Events Coordinator</li>
      <li>Drivers<span class="note">(must have personal car,&nbsp; insurance &amp; Driver’s License)</span></li>
      <li>Outreach Specialist - Walkers</li>
      <li>Outreach Specialist - Phone/ Telemarketing<span class="note">(evenings only)</span></li>
    </ul>
  </section>
  <aside class="perks">
    <svg viewBox="0 0 217 206" preserveAspectRatio="none" aria-hidden="true"><polygon points="0,14 175,14 197,0 217,12 217,206 0,206" fill="#1d3a70"/></svg>
    <ul>
      <li>Excellent Pay !</li>
      <li>Fun Atmosphere</li>
      <li>Bonus Pay with Promotional<br>&amp; Career Advancement<br>Opportunities</li>
    </ul>
    <p class="contact">Questions call Renata Cole at</p>
    <p class="phone"><svg viewBox="0 0 24 24" aria-hidden="true"><circle cx="12" cy="12" r="11" fill="none" stroke="#fff" stroke-width="2"/><path d="M8 6l2 0 1 3-1.5 1.2a8 8 0 0 0 4.3 4.3L15 13l3 1v2c0 1-1 2-2 2A10 10 0 0 1 6 8c0-1 1-2 2-2z" fill="#fff"/></svg>909.555.0142</p>
  </aside>
  <address class="board">Ridgeview County<br>Workforce Board<div class="street">412 West Oak Lane (Suite 200)<br>Ridgeview, CA 92410</div></address>
  <div class="badge"></div>
</article>

<article class="flyer flyer--8x11">
  <div class="photo" role="img" aria-label="Smiling young professional in a grey pinstripe suit and tie"></div>
  <div class="flag" role="img" aria-label="Waving American flag"></div>
  <h1 class="headline"><span class="were">WE’RE</span><span class="hiring">HIRING</span></h1>
  <p class="candidate"><span class="mark"></span><span class="name">Marco<br>Delgado<br>Mayor</span></p>
  <section class="positions">
    <h2>JOB POSITIONS INCLUDE:</h2>
    <ul>
      <li>Office Manager</li>
      <li>Office Assistant</li>
      <li>Data Entry Techs</li>
      <li>Outreach Manager</li>
      <li>Asst. Outreach Manager</li>
      <li>Events Coordinator</li>
      <li>Drivers<span class="note">(must have personal car,&nbsp; insurance &amp; Driver’s License)</span></li>
      <li>Outreach Specialist - Walkers</li>
      <li>Outreach Specialist - Phone/ Telemarketing<span class="note">(evenings only)</span></li>
    </ul>
  </section>
  <aside class="perks">
    <svg viewBox="0 0 217 206" preserveAspectRatio="none" aria-hidden="true"><polygon points="0,14 175,14 197,0 217,12 217,206 0,206" fill="#1d3a70"/></svg>
    <ul>
      <li>Excellent Pay !</li>
      <li>Fun Atmosphere</li>
      <li>Bonus Pay with Promotional<br>&amp; Career Advancement<br>Opportunities</li>
    </ul>
    <p class="contact">Questions call Renata Cole at</p>
    <p class="phone"><svg viewBox="0 0 24 24" aria-hidden="true"><circle cx="12" cy="12" r="11" fill="none" stroke="#fff" stroke-width="2"/><path d="M8 6l2 0 1 3-1.5 1.2a8 8 0 0 0 4.3 4.3L15 13l3 1v2c0 1-1 2-2 2A10 10 0 0 1 6 8c0-1 1-2 2-2z" fill="#fff"/></svg>909.555.0142</p>
  </aside>
  <address class="board">Ridgeview County<br>Workforce Board<div class="street">412 West Oak Lane (Suite 200)<br>Ridgeview, CA 92410</div></address>
  <div class="badge"></div>
</article>

</body>
</html>
```